TK Workshop - flyer

We are a machine shop. While making sales calls in the field, we need a flyer to leave behind with prospect to attract interest.

Target Market(s)

Medical device, aerospace and aviation component manfacturers

Font styles to use
Serif

Colors

Designer to choose colors to be used in the design.

Requirements
Must have
• NA
Nice to have
• NA
Should not have
• NA

```html
<!DOCTYPE html>
<html lang="en">
<head>
<meta charset="utf-8">
<title>TK Workshop – Titanium Spinal Screw Assemblies</title>
<link href="https://fonts.googleapis.com/css2?family=Raleway:wght@300;400;700&family=Open+Sans:wght@400;700&family=Roboto:wght@400&display=swap" rel="stylesheet">
<style>
  :root{
    --red:#e31e26;
    --ink:#2b2b2d;
    --grey-text:#5b5b5d;
    --footer:#3a3a3c;
    --hex-dark:#3d3d3f;
    --white:#ffffff;
    --paper:#f7f7f7;
    --stage:#8d8787;
  }
  html,body{margin:0;padding:0;width:946px;height:1200px;overflow:hidden;background:var(--stage);}
  .flyer{
    position:absolute;left:49px;top:0;width:939px;height:1328px;
    transform:scale(0.9036);transform-origin:0 0;overflow:hidden;
    font-family:"Raleway",sans-serif;background:var(--white);
  }
  .shapes{position:absolute;left:0;top:0;width:939px;height:1328px;}
  .abs{position:absolute;margin:0;}
  .brand{left:50px;top:118px;display:flex;align-items:center;gap:14px;}
  .brand-name{font-family:"Raleway",sans-serif;font-weight:400;font-size:50px;color:var(--ink);letter-spacing:-1px;}
  .brand-dot{width:54px;height:54px;border-radius:50%;background:var(--red);}
  .headline{right:37px;top:78px;text-align:right;color:var(--white);font-weight:400;font-size:60px;line-height:66px;}
  .headline .accent{display:block;color:var(--red);font-weight:700;}
  .headline-rule{left:823px;top:284px;width:76px;height:3px;background:var(--red);}
  .intro{right:36px;top:297px;width:312px;text-align:right;color:var(--white);font-weight:300;font-size:17.5px;line-height:21.6px;}
  .cap-title{left:65px;top:694px;font-size:38px;line-height:42px;color:var(--ink);font-weight:400;}
  .cap-title strong{display:block;color:var(--red);font-weight:700;}
  .cap-rule{left:65px;top:784px;width:66px;height:4px;background:var(--grey-text);}
  .cap-lead{left:65px;top:800px;width:460px;font-size:24px;line-height:30px;color:var(--grey-text);font-weight:300;}
  .cap-list{left:65px;top:882px;list-style:none;padding:0;}
  .cap-list li{display:flex;align-items:center;height:45.7px;font-size:24px;color:var(--grey-text);}
  .cap-list svg{width:26px;height:26px;margin-right:34px;}
  .hex-text{position:absolute;margin:0;text-align:center;font-family:"Open Sans",sans-serif;color:var(--white);font-size:15px;line-height:21.5px;}
  .hex-text b{color:var(--red);font-size:17px;}
  .hex-text .dark{color:var(--hex-dark);font-size:16px;}
  .markets{left:65px;top:1172px;font-size:24px;color:var(--red);}
  .certs{left:65px;top:1204px;font-size:30px;font-weight:700;color:var(--ink);}
  .footer-text{font-family:"Roboto",sans-serif;font-size:19px;line-height:25px;color:var(--white);}
</style>
</head>
<body>
<div class="flyer">
  <svg class="shapes" viewBox="0 0 939 1328">
    <defs>
      <radialGradient id="workshop" cx="0.7" cy="0.45" r="0.7">
        <stop offset="0" stop-color="#5e4a34"/>
        <stop offset="0.6" stop-color="#32261d"/>
        <stop offset="1" stop-color="#1e1814"/>
      </radialGradient>
      <linearGradient id="parts" x1="0" y1="0" x2="1" y2="1">
        <stop offset="0" stop-color="#f2f2f4"/>
        <stop offset="0.5" stop-color="#e3e7ea"/>
        <stop offset="1" stop-color="#eef1ec"/>
      </linearGradient>
    </defs>
    <rect role="img" aria-label="Dim machine shop interior with CNC equipment" width="939" height="920" fill="url(#workshop)"/>
    <polygon points="0,0 354,0 451,148 379,285 0,285" fill="var(--paper)"/>
    <polygon points="0,285 517,285 624,473 517,665 0,665" fill="var(--red)"/>
    <polygon role="img" aria-label="Titanium spinal screws with coloured anodised tulip heads" points="0,295 508,295 608,473 508,655 0,655" fill="url(#parts)"/>
    <polygon points="0,665 512,665 939,918 939,1250 0,1250" fill="var(--white)"/>
    <polygon points="520,655 939,897 939,912 505,664" fill="var(--red)"/>
    <polygon points="437,936 555,862 673,936 673,1062 555,1132 437,1062" fill="var(--hex-dark)" stroke="var(--red)" stroke-width="3"/>
    <polygon points="682,936 799,862 917,936 917,1062 799,1132 682,1062" fill="var(--hex-dark)" stroke="var(--red)" stroke-width="3"/>
    <polygon points="679,640 800,710 800,850 679,917 559,850 559,710" fill="var(--red)"/>
    <g fill="var(--white)">
      <rect x="616" y="723" width="128" height="9" rx="3"/>
      <rect x="617" y="708" width="8" height="55"/>
      <rect x="632" y="712" width="6" height="30"/>
      <rect x="652" y="720" width="20" height="22" rx="2"/>
      <rect x="664" y="732" width="7" height="30"/>
      <circle cx="696" cy="737" r="5"/>
    </g>
    <g fill="none" stroke="var(--white)" stroke-width="4" stroke-linecap="round">
      <path d="M530 956 l20 -20 l22 14 l-6 30 l-20 4 z" fill="var(--white)"/>
      <path d="M572 925 l14 -6 M566 916 l6 -10"/>
    </g>
    <g fill="none" stroke="var(--white)" stroke-width="3">
      <rect x="792" y="905" width="12" height="50" rx="6"/>
      <circle cx="798" cy="964" r="11" fill="var(--white)"/>
      <path d="M808 925 l26 -22 M770 950 h18"/>
    </g>
    <rect x="0" y="1250" width="939" height="78" fill="var(--footer)"/>
    <rect x="0" y="1246" width="769" height="8" fill="var(--red)"/>
    <g fill="none" stroke="var(--red)" stroke-width="3">
      <path d="M79 1307 c-10 -12 -13 -18 -13 -23 a13 13 0 0 1 26 0 c0 5 -3 11 -13 23 z"/>
      <circle cx="79" cy="1284" r="4"/>
      <circle cx="562" cy="1280" r="10"/>
      <circle cx="562" cy="1313" r="10"/>
    </g>
    <circle cx="562" cy="1280" r="5" fill="var(--red)"/>
    <path d="M557 1309 l3 -2 l2 3 l-2 2 q2 3 4 4 l2 -2 l3 2 l-2 3 q-7 -1 -10 -10 z" fill="var(--red)"/>
  </svg>

  <div class="abs brand"><span class="brand-name">TK Workshop</span><span class="brand-dot"></span></div>

  <h1 class="abs headline">Titanium<br>Spinal Screw<span class="accent">Assemblies</span></h1>
  <div class="abs headline-rule"></div>
  <p class="abs intro">Our Education, Training, and 25 years of Medical and Aerospace machining experience helps us determine the best possible methods of manufacture that will be most cost effective for your parts.</p>

  <h2 class="abs cap-title">OUR<strong>CAPABILITIES</strong></h2>
  <div class="abs cap-rule"></div>
  <p class="abs cap-lead">We make the parts, process them, and assemble them.</p>
  <ul class="abs cap-list">
    <li><svg viewBox="0 0 26 26"><path d="M4 14 l6 6 l12 -14" fill="none" stroke="var(--red)" stroke-width="3"/></svg>5 axis cnc milling</li>
    <li><svg viewBox="0 0 26 26"><path d="M4 14 l6 6 l12 -14" fill="none" stroke="var(--red)" stroke-width="3"/></svg>Turning</li>
    <li><svg viewBox="0 0 26 26"><path d="M4 14 l6 6 l12 -14" fill="none" stroke="var(--red)" stroke-width="3"/></svg>Cnc swiss-type</li>
    <li><svg viewBox="0 0 26 26"><path d="M4 14 l6 6 l12 -14" fill="none" stroke="var(--red)" stroke-width="3"/></svg>Deburring</li>
    <li><svg viewBox="0 0 26 26"><path d="M4 14 l6 6 l12 -14" fill="none" stroke="var(--red)" stroke-width="3"/></svg>Vistametric scope 302</li>
    <li><svg viewBox="0 0 26 26"><path d="M4 14 l6 6 l12 -14" fill="none" stroke="var(--red)" stroke-width="3"/></svg>Laser marking</li>
  </ul>

  <p class="hex-text" style="left:574px;top:780px;width:210px;">Coordinate <span class="dark">Measuring</span><br>machines, comparators,<br>sur-face plated<br>micrometers</p>
  <p class="hex-text" style="left:455px;top:1000px;width:200px;">Ultrasonic<br><b>Cleaning &amp; Reverse</b><br>osmosis water</p>
  <p class="hex-text" style="left:690px;top:1000px;width:220px;">Dedicated<br><b>Temperature Controlled</b><br>room</p>

  <p class="abs markets">Medical, Implants, Aerospace, Aviation &amp; Military applications</p>
  <p class="abs certs">ISO 13485, 9100, 9001 CERTIFIED</p>

  <p class="abs footer-text" style="left:120px;top:1260px;">4410 Birch Lane, Unit B,<br>Valley Ridge, CA 90210</p>
  <p class="abs footer-text" style="left:593px;top:1268px;">www.tkworkshopcnc.com</p>
  <p class="abs footer-text" style="left:593px;top:1301px;">(555) 014-2290</p>
</div>
</body>
</html>
```